Modern brochure by Lawyers, for modern clients

It'sa "News" for their clients. Attached you can find the current News without design. It must be elegant but very attractive and modern. Their web site is http://www.montalbanyasociados.cl/ Their expertise is labor and employment practice area. It must be in editable format so that lawyers can write the news in a template with this corporate design.

Target Market(s)

Big Companies

Font styles to use
Sans Serif

Colors
0255a3
474747

Requirements
Nice to have
• Legal Pictures and only a little of yellow. One touch! It must be in editable format so that lawyers can write the news in a template with this corporate design.

```html
<!DOCTYPE html>
<html lang="es">
<head>
<meta charset="utf-8">
<title>Montalbán y Asociados Abogados · Noticias</title>
<link href="https://fonts.googleapis.com/css2?family=Lato:wght@300;400;700;900&display=swap" rel="stylesheet">
<style>
  :root{
    --navy:#3c5673;
    --steel:#7a93a7;
    --mist:#a9bccb;
    --haze:#dbe4ea;
    --ink:#1c1c1c;
    --grey:#6b6b6b;
    --paper:#ffffff;
    --photo-a:#1f4f9c;
    --photo-b:#6f93c9;
  }
  *{margin:0;padding:0;box-sizing:border-box}
  html,body{width:1048px;height:1200px;overflow:hidden;background:var(--paper)}
  body{font-family:"Lato",sans-serif;color:var(--ink);position:relative}

  .top-band{position:absolute;left:0;top:0;width:1048px;height:13px;background:var(--navy)}

  .brand{position:absolute;left:62px;top:50px;display:flex;align-items:center;gap:14px}
  .brand-dot{width:62px;height:62px;border-radius:50%;background:var(--navy);flex:none}
  .brand-name{font-weight:300;color:var(--navy);line-height:1.05;letter-spacing:1px}
  .brand-name .l1{display:block;font-size:40px}
  .brand-name .l2{display:block;font-size:26px}

  .date{position:absolute;right:50px;top:96px;font-size:17px;color:var(--grey);font-weight:400}

  .side-block{position:absolute;background:var(--navy)}
  .side-block.left{left:0;top:150px;width:77px;height:341px}
  .side-block.right{left:971px;top:861px;width:77px;height:339px}

  .hero{position:absolute;left:132px;top:147px;width:916px;height:339px}
  .hero svg{position:absolute;inset:0}
  .hero-copy{position:absolute;left:50px;top:94px;width:440px;color:#fff}
  .hero-title{font-size:32px;font-weight:900;letter-spacing:.5px;padding-bottom:10px;border-bottom:2px solid #fff;width:303px}
  .hero-text{margin-top:22px;font-size:20.5px;font-weight:700;line-height:24px}

  .divider{position:absolute;left:139px;width:303px;height:7px;display:flex}
  .divider span{flex:1}
  .divider span:nth-child(1){background:var(--navy)}
  .divider span:nth-child(2){background:var(--steel)}
  .divider span:nth-child(3){background:var(--mist)}
  .divider span:nth-child(4){background:var(--haze)}

  .body{position:absolute;left:138px;top:563px;width:830px;font-size:17.5px;line-height:21px}
  .body p{margin-bottom:17px}
  .body .lead{font-weight:700}

  .closing{position:absolute;left:138px;top:893px;width:560px;color:var(--grey);font-weight:700;font-size:19.5px;line-height:24px}
  .closing p + p{margin-top:24px}

  .footer-url{position:absolute;left:0;width:1048px;top:1094px;text-align:center;font-size:17px;font-weight:700;color:var(--navy)}
  .footer-brand{position:absolute;left:434px;top:1118px;display:flex;align-items:center;gap:7px}
  .footer-brand .brand-dot{width:32px;height:32px}
  .footer-brand .brand-name .l1{font-size:20px}
  .footer-brand .brand-name .l2{font-size:13px}
</style>
</head>
<body>
  <div class="top-band"></div>

  <header class="brand">
    <div class="brand-dot"></div>
    <div class="brand-name"><span class="l1">MONTALBÁN</span><span class="l2">Y ASOCIADOS ABOGADOS</span></div>
  </header>
  <div class="date">Santiago, 25 de julio de 2018</div>

  <div class="side-block left"></div>

  <section class="hero">
    <svg width="916" height="339" viewBox="0 0 916 339">
      <defs>
        <linearGradient id="towerTone" x1="0" y1="0" x2="1" y2="1">
          <stop offset="0" stop-color="var(--photo-b)"/>
          <stop offset=".55" stop-color="var(--photo-a)"/>
          <stop offset="1" stop-color="#3b6b3a"/>
        </linearGradient>
      </defs>
      <rect x="400" y="0" width="516" height="339" fill="url(#towerTone)" role="img" aria-label="Fotografía de un edificio corporativo de fachada de vidrio con árboles en primer plano"/>
      <polygon points="0,0 492,0 596,172 463,339 0,339" fill="var(--navy)"/>
    </svg>
    <div class="hero-copy">
      <h1 class="hero-title">ESTIMADOS,</h1>
      <p class="hero-text">Por medio del presente, les damos a conocer el Dictamen Ordinario N° 3826-031, emitido por la Dirección del Trabajo el pasado 20 de julio, relativo a los “beneficios históricos”.</p>
    </div>
  </section>

  <div class="divider" style="top:536px"><span></span><span></span><span></span><span></span></div>

  <article class="body">
    <p class="lead">Estos fueron definidos en su oportunidad por este organismo como “...aquellos beneficios que se han otorgado desde siempre...” por parte del empleador.</p>
    <p>A partir de este Dictamen, el cual reconsidera el criterio del anterior Director del Trabajo, los beneficios históricos vuelven a ser patrimonio de la empresa y de los trabajadores que los han recibido, dejando de serlo de la organización sindical y de sus socios beneficiados por el solo hecho de haberse “replicado” en un instrumento colectivo durante una negociación.</p>
    <p>Por último, el Dictamen en comento aclara que si un “beneficio histórico” se incrementa de manera real y efectiva producto de una negociación colectiva, únicamente dicho incremento se entenderá originado en el respectivo instrumento colectivo, y en consecuencia, objeto de una posible extensión en el evento de que ésta se haya acordado durante la negociación.</p>
  </article>

  <div class="side-block right"></div>

  <section class="closing">
    <p>Para mayor análisis de lo resuelto por la Dirección del Trabajo, se puede revisar el Dictámen en comento haciendo click aquí</p>
    <p>Sin otro particular saluda atentamente a usted,</p>
  </section>

  <div class="divider" style="top:1026px"><span></span><span></span><span></span><span></span></div>

  <footer>
    <div class="footer-url">www.montalbanyasociados.cl</div>
    <div class="footer-brand">
      <div class="brand-dot"></div>
      <div class="brand-name"><span class="l1">MONTALBÁN</span><span class="l2">Y ASOCIADOS ABOGADOS</span></div>
    </div>
  </footer>
</body>
</html>
```